Business Cards/Stationary/Letterhead for Crestline Weight Loss Center
Be Healthy, Be Fit, and Be Ready to Lose Weight!
Creative Brief
Simple
Derek Tolsan, PA
Physician Assistant, Co-founder
52816 Birchwood Lane Fremont, CA 94592-7731
CrestlineSlim@mailhaven.example
www.crestlineslim.example
Aim for Results with Crestline Weight Loss! HCG, Appetite Suppressants,B12/B-Complex injections, Menu Plans, Exercise Plans, Nutriceuticals, Supplements.
Present this card to a friend; If your friend signs up, you will receive a 20% discount. The referrals are endless. If you refer 5 friends who sign up then you will receive 100% discount on your next visit. Just make sure your friend puts your name down in the "referral" section of the information sheet and you will be that much closer to saving. (Discount will only apply to weight loss program, discount only applicable for one month or week supply of medication. Non-transferrable. Referral cannot be an existing patient.) Appointment Date: _________ Time: _____

```html
<!DOCTYPE html>
<html lang="en">
<head>
<meta charset="utf-8">
<title>Crestline Weight Loss Center – Stationery Set</title>
<link href="https://fonts.googleapis.com/css2?family=Arimo:wght@400;700&display=swap" rel="stylesheet">
<style>
  :root {
    --backdrop: #c9c9ca;
    --paper: #ffffff;
    --ink: #1b1b1b;
    --grey-text: #6d6e71;
    --brand-green: #8dc63f;
    --brand-orange: #f7941d;
    --hairline: #d4d4d4;
  }
  * { margin: 0; padding: 0; box-sizing: border-box; }
  html, body { width: 1200px; height: 666px; overflow: hidden; }
  body {
    background: var(--backdrop);
    font-family: "Arimo", Arial, sans-serif;
    color: var(--ink);
    position: relative;
  }
  .sheet {
    position: absolute;
    background: var(--paper);
    box-shadow: 0 1px 3px rgba(0,0,0,.22);
    overflow: hidden;
  }
  .sheet svg.shape { position: absolute; left: 0; width: 100%; }

  .brand { display: flex; align-items: center; gap: 5px; }
  .brand-dot { border-radius: 50%; background: var(--brand-green); flex: none; }
  .brand-name { color: var(--brand-green); font-weight: 700; white-space: nowrap; }

  /* Envelopes */
  .envelope-dark { left: 53px; top: 29px; width: 374px; height: 187px; }
  .envelope-light { left: 53px; top: 228px; width: 374px; height: 185px; }
  .envelope .brand { position: absolute; left: 50%; transform: translateX(-50%); flex-direction: column; gap: 3px; }
  .envelope-dark .brand { top: 76px; }
  .envelope-light .brand { top: 62px; }
  .envelope .brand-dot { width: 16px; height: 16px; }
  .envelope .brand-name { font-size: 9px; }
  .envelope .web { position: absolute; left: 0; right: 0; text-align: center; font-size: 5px; color: var(--grey-text); }
  .envelope-dark .web { top: 125px; }

  /* Compliment slip */
  .slip { left: 53px; top: 425px; width: 374px; height: 209px; }
  .slip .brand { position: absolute; left: 22px; top: 20px; flex-direction: column; align-items: flex-start; gap: 3px; }
  .slip .brand-dot { width: 16px; height: 16px; }
  .slip .brand-name { font-size: 9px; }
  .slip .address { position: absolute; left: 22px; top: 70px; font-size: 5px; line-height: 1.5; color: var(--grey-text); }

  /* Letterheads */
  .letterhead { top: 120px; width: 343px; height: 514px; }
  .letterhead-left { left: 449px; }
  .letterhead-right { left: 816px; }
  .letterhead .brand { position: absolute; top: 26px; flex-direction: column; gap: 3px; }
  .letterhead-left .brand { left: 28px; align-items: flex-start; }
  .letterhead-right .brand { left: 50%; transform: translateX(-50%); }
  .letterhead .brand-dot { width: 18px; height: 18px; }
  .letterhead .brand-name { font-size: 10px; }
  .letterhead .contact { position: absolute; font-size: 5px; line-height: 1.55; color: var(--grey-text); }
  .letterhead-left .contact { left: 232px; top: 30px; }
  .letterhead .contact .accent { color: var(--brand-orange); }
  .letterhead .footer-contact { position: absolute; right: 22px; bottom: 8px; font-size: 5px; line-height: 1.55; color: var(--paper); text-align: right; }

  /* Business cards */
  .card { top: 29px; height: 77px; border-radius: 5px; }
  .card-front-a { left: 470px; width: 159px; }
  .card-back-a { left: 634px; width: 158px; }
  .card-front-b { left: 816px; width: 149px; }
  .card-back-b { left: 970px; width: 158px; }
  .card .person { position: absolute; right: 8px; top: 7px; text-align: right; font-size: 5px; line-height: 1.4; color: var(--grey-text); }
  .card .person strong { display: block; color: var(--ink); font-size: 6px; }
  .card .details { position: absolute; right: 8px; bottom: 7px; text-align: right; font-size: 4px; line-height: 1.45; color: var(--grey-text); }
  .card .brand { position: absolute; left: 8px; top: 24px; }
  .card .brand-dot { width: 10px; height: 10px; }
  .card .brand-name { font-size: 5.5px; }
  .card-back .band { position: absolute; left: 0; top: 0; width: 100%; height: 20px; background: var(--brand-green); display: flex; align-items: center; padding: 0 8px; gap: 4px; }
  .card-back .band .brand-dot { width: 9px; height: 9px; background: var(--paper); border-radius: 50%; }
  .card-back .band span { color: var(--paper); font-size: 5.5px; font-weight: 700; }
  .card-back .referral { position: absolute; left: 8px; right: 8px; top: 24px; font-size: 3.4px; line-height: 1.35; color: var(--grey-text); }
  .card-back .appointment { position: absolute; left: 8px; bottom: 6px; font-size: 4px; color: var(--ink); }
</style>
</head>
<body>

  <!-- Envelope with dark flap -->
  <section class="sheet envelope envelope-dark">
    <svg class="shape" style="top:0;height:187px" viewBox="0 0 374 187" preserveAspectRatio="none" aria-hidden="true">
      <path d="M0 0 H374 V22 C300 30 230 60 187 68 C144 60 74 30 0 22 Z" fill="var(--ink)"/>
    </svg>
    <div class="brand">
      <span class="brand-dot"></span>
      <span class="brand-name">Crestline Weight Loss Center</span>
    </div>
    <p class="web">www.crestlineslim.example</p>
  </section>

  <!-- Envelope with line flap -->
  <section class="sheet envelope envelope-light">
    <svg class="shape" style="top:0;height:185px" viewBox="0 0 374 185" preserveAspectRatio="none" aria-hidden="true">
      <path d="M0 0 C90 28 150 50 187 56 C224 50 284 28 374 0" fill="none" stroke="var(--hairline)" stroke-width="1"/>
    </svg>
    <div class="brand">
      <span class="brand-dot"></span>
      <span class="brand-name">Crestline Weight Loss Center</span>
    </div>
  </section>

  <!-- Compliment slip -->
  <section class="sheet slip">
    <div class="brand">
      <span class="brand-dot"></span>
      <span class="brand-name">Crestline Weight Loss Center</span>
    </div>
    <p class="address">52816 Birchwood Lane<br>Fremont, CA 94592-7731</p>
    <svg class="shape" style="bottom:0;height:50px" viewBox="0 0 374 50" preserveAspectRatio="none" aria-hidden="true">
      <path d="M0 24 C90 6 170 40 374 14 V50 H0 Z" fill="var(--ink)"/>
      <path d="M0 22 C90 4 170 38 374 12" fill="none" stroke="var(--brand-orange)" stroke-width="3"/>
      <path d="M0 30 C100 14 180 44 374 22" fill="none" stroke="var(--brand-green)" stroke-width="2"/>
    </svg>
  </section>

  <!-- Business card pair A -->
  <section class="sheet card card-front-a">
    <div class="person"><strong>Derek Tolsan, PA</strong>Physician Assistant, Co-founder</div>
    <div class="brand">
      <span class="brand-dot"></span>
      <span class="brand-name">Crestline Weight Loss</span>
    </div>
    <div class="details">52816 Birchwood Lane Fremont, CA 94592-7731<br>510.555.0184<br>CrestlineSlim@mailhaven.example<br>www.crestlineslim.example</div>
  </section>
  <section class="sheet card card-back card-back-a">
    <div class="band"><span class="brand-dot"></span><span>Crestline Weight Loss</span></div>
    <p class="referral">Aim for Results with Crestline Weight Loss! HCG, Appetite Suppressants, B12/B-Complex injections, Menu Plans, Exercise Plans, Nutriceuticals, Supplements.</p>
  </section>

  <!-- Business card pair B -->
  <section class="sheet card card-front-b">
    <div class="person"><strong>Derek Tolsan, PA</strong>Physician Assistant, Co-founder</div>
    <div class="brand">
      <span class="brand-dot"></span>
      <span class="brand-name">Crestline Weight Loss</span>
    </div>
    <div class="details">52816 Birchwood Lane Fremont, CA 94592-7731<br>510.555.0184<br>CrestlineSlim@mailhaven.example</div>
  </section>
  <section class="sheet card card-back card-back-b">
    <div class="band"><span class="brand-dot"></span><span>Crestline Weight Loss</span></div>
    <p class="referral">Present this card to a friend; If your friend signs up, you will receive a 20% discount. If you refer 5 friends who sign up then you will receive 100% discount on your next visit. Referral cannot be an existing patient.</p>
    <p class="appointment">Appointment Date: _________ Time: _____</p>
  </section>

  <!-- Letterhead, left-aligned -->
  <section class="sheet letterhead letterhead-left">
    <div class="brand">
      <span class="brand-dot"></span>
      <span class="brand-name">Crestline Weight Loss Center</span>
    </div>
    <div class="contact">
      52816 Birchwood Lane<br>Fremont, CA 94592-7731<br>
      <span class="accent">Phone: 510.555.0184</span><br>
      <span class="accent">CrestlineSlim@mailhaven.example</span>
    </div>
    <svg class="shape" style="bottom:0;height:80px" viewBox="0 0 343 80" preserveAspectRatio="none" aria-hidden="true">
      <path d="M0 36 C80 10 160 60 343 20 V80 H0 Z" fill="var(--ink)"/>
      <path d="M0 34 C80 8 160 58 343 18" fill="none" stroke="var(--brand-orange)" stroke-width="4"/>
      <path d="M0 44 C90 22 170 66 343 30" fill="none" stroke="var(--brand-green)" stroke-width="2.5"/>
    </svg>
    <p class="footer-contact">www.crestlineslim.example</p>
  </section>

  <!-- Letterhead, centred -->
  <section class="sheet letterhead letterhead-right">
    <div class="brand">
      <span class="brand-dot"></span>
      <span class="brand-name">Crestline Weight Loss Center</span>
    </div>
    <svg class="shape" style="bottom:0;height:80px" viewBox="0 0 343 80" preserveAspectRatio="none" aria-hidden="true">
      <path d="M0 36 C80 10 160 60 343 20 V80 H0 Z" fill="var(--ink)"/>
      <path d="M0 34 C80 8 160 58 343 18" fill="none" stroke="var(--brand-orange)" stroke-width="4"/>
      <path d="M0 44 C90 22 170 66 343 30" fill="none" stroke="var(--brand-green)" stroke-width="2.5"/>
    </svg>
    <p class="footer-contact">52816 Birchwood Lane Fremont, CA 94592-7731<br>Phone: 510.555.0184 · Fax: 510.555.0185<br>CrestlineSlim@mailhaven.example</p>
  </section>

</body>
</html>
```